I am a highly experienced private practice psychotherapist serving high end clientele in the Wall Street area of New York City. I need electronic letterhead (that can also be printed) to use for bills, receipts, and correspondences.
Updates

My clients are very high end and are used to elegance and wealth. The letterhead should contain the following information: Marian T. Folsom, LCSW 84 Hollis Lane, Suite 2716 New York, NY 10092 Phone : (917) 555-3019 email: therapy@marianfolsomlcsw.example website: www.marianfolsomlcsw.example

Thank you for your designs. Please be advised that the letterhead will be used for bills/invoices; professional letters to other mental health professionals and doctors, as well as to attorneys. It needs to be highly professional in the same way that a law firm has professional and elegant letterhead, raher than whimsical or with spa designers. My letters end up as official documents.

Industry/Entity Type

Electronic

```html
<!DOCTYPE html>
<html lang="en">
<head>
<meta charset="utf-8">
<title>Marian T. Folsom, LCSW — Letterhead</title>
<link rel="stylesheet" href="https://fonts.googleapis.com/css2?family=Cormorant+Garamond:wght@400;500&family=Crimson+Text&family=Raleway:wght@400;500&display=swap">
<style>
  :root {
    --paper: #ffffff;
    --name-blue: #5b93ad;
    --tagline-blue: #72a8c1;
    --ink-navy: #1f3447;
    --band-blue: #68a0b9;
  }
  html, body {
    margin: 0;
    padding: 0;
    overflow: hidden;
    background: var(--paper);
  }
  .letterhead {
    position: relative;
    width: 927px;
    height: 1200px;
    background: var(--paper);
    overflow: hidden;
  }
  .masthead {
    position: absolute;
    top: 34px;
    left: 0;
    width: 100%;
    text-align: center;
  }
  .practitioner-name {
    margin: 0;
    font-family: "Cormorant Garamond", serif;
    font-weight: 500;
    font-size: 31px;
    letter-spacing: 0.5px;
    line-height: 1;
    color: var(--name-blue);
  }
  .discipline {
    margin: 20px 0 0;
    font-family: "Raleway", sans-serif;
    font-weight: 500;
    font-size: 13px;
    letter-spacing: 0.4px;
    line-height: 1;
    color: var(--ink-navy);
  }
  .specialties {
    margin: 5px 0 0;
    font-family: "Raleway", sans-serif;
    font-weight: 400;
    font-size: 13px;
    letter-spacing: 0.4px;
    line-height: 1;
    color: var(--tagline-blue);
  }
  .contact-block {
    position: absolute;
    top: 1027px;
    left: 0;
    width: 100%;
    text-align: center;
    font-family: "Crimson Text", serif;
    color: var(--ink-navy);
    font-style: normal;
  }
  .contact-block p { margin: 0; }
  .address-line {
    font-size: 16px;
    line-height: 20px;
  }
  .phone {
    margin-top: 25px !important;
    font-size: 18.5px;
    line-height: 22px;
  }
  .web-line {
    font-size: 15px;
    line-height: 20px;
  }
  .phone + .web-line { margin-top: 4px; }
  .footer-band {
    position: absolute;
    left: 0;
    bottom: 0;
    width: 100%;
    height: 22px;
    background: var(--band-blue);
  }
</style>
</head>
<body>
  <main class="letterhead">
    <header class="masthead">
      <h1 class="practitioner-name">Marian T. Folsom, LCSW</h1>
      <p class="discipline">PSYCHOTHERAPY</p>
      <p class="specialties">INDIVIDUAL - FAMILY - RELATIONSHIP</p>
    </header>

    <address class="contact-block">
      <p class="address-line">84 Hollis Lane, Suite 2716</p>
      <p class="address-line">New York, NY 10092</p>
      <p class="phone">(917) 555-3019</p>
      <p class="web-line">therapy@marianfolsomlcsw.example</p>
      <p class="web-line">www.marianfolsomlcsw.example</p>
    </address>

    <div class="footer-band"></div>
  </main>
</body>
</html>
```